Recruitment Site Design

We need a design for the login page, about page, and inner pages of a recruitment site for an oil and gas company. Design should be modern, sleek, professional and colors can be blue, green, white, orange or any other recommended colors.

Please also take into consideration that once the users login, they will need to access a form to fill in their information.

** UPDATE: Kindly provide a design for the inner information page consistent with the outer design. Attached is a picture of the basic structure. ***
Updates

Please provide a design for inner pages as shown in the design brief consistent with the registration page provided. 

Reason: We're extending it to get more inside pages.

Target Market(s)

Professionals looking for a career in the oil and gas industry in the Middle East.

Industry/Entity Type

Oil And Gas

Requirements
Must have
• Sleek design

```html
<!DOCTYPE html>
<html lang="en">
<head>
<meta charset="utf-8">
<title>About Us – Petrova Careers</title>
<link href="https://fonts.googleapis.com/css2?family=Arimo:wght@400;700&family=PT+Sans+Narrow:wght@400;700&family=Tinos:wght@700&display=swap" rel="stylesheet">
<style>
:root{
  --header-blue:#1258a6;
  --nav-top:#5fc3f2;
  --nav-bottom:#1a94d8;
  --page-bg:#ebe9ea;
  --accent:#1ba3e0;
  --text:#5e5e60;
  --link:#0d56a6;
  --rule:#b9b7b8;
  --footer-band:#58585a;
  --footer-bg:#a3a3a5;
  --footer-text:#ffffff;
  --legal-bg:#003a7a;
  --photo-tone:#9c9ea3;
}
*{margin:0;padding:0;box-sizing:border-box}
html,body{width:1200px;height:1200px;overflow:hidden}
body{position:relative;background:var(--page-bg);font-family:"Arimo",Arial,sans-serif;color:var(--text)}
.abs{position:absolute}
.site-header{left:0;top:0;width:1200px;height:66px;background:var(--header-blue)}
.brand{left:188px;top:10px;font-size:36px;font-weight:700;color:#d8dbe0;letter-spacing:.5px}
.account-links{left:829px;top:19px;font-size:12px;color:#fff;word-spacing:4px}
.main-nav{left:0;top:66px;width:1200px;height:40px;background:linear-gradient(var(--nav-top),var(--nav-bottom));border-top:2px solid #9fdcf8}
.main-nav ul{list-style:none;display:flex;align-items:center;height:100%;padding-left:202px}
.main-nav li{font-size:13px;font-weight:700;color:#fff;margin-right:26px}
.main-nav li.current{color:#111}
.main-nav svg{display:block}
.page-title{left:183px;top:164px;font-size:30px;font-weight:700;color:var(--accent)}
.intro{left:182px;top:216px;width:800px;font-size:14px;line-height:17.7px;text-align:justify}
.intro p{margin-bottom:17.7px}
.intro a{color:var(--link);text-decoration:none}
.rule{height:1px;background:linear-gradient(90deg,transparent,var(--rule) 12%,var(--rule) 88%,transparent)}
.mission-title{left:192px;top:449px;width:180px;text-align:center;font-family:"Tinos",serif;font-weight:700;font-size:29px;line-height:30px;color:var(--accent)}
.mission-quote{left:402px;top:461px;width:540px;font-family:"Tinos",serif;font-weight:700;font-size:22px;line-height:22px;color:#6b6b6d}
.section-title{font-size:20px;font-weight:700;color:var(--accent)}
.team-photo{width:90px;height:90px;border:1px solid #8a8a8a;background:linear-gradient(160deg,#c9cacd,var(--photo-tone) 55%,#4a4d55)}
.role{font-size:19px;color:var(--accent)}
.bio{width:550px;font-size:14px;line-height:17.7px}
.info-head{font-size:18px;color:var(--accent)}
.info-label{font-size:17px;color:var(--accent)}
.info-text{font-size:14px;line-height:23px}
.footer-band{left:0;top:1018px;width:1200px;height:5px;background:var(--footer-band)}
.site-footer{left:0;top:1023px;width:1200px;height:150px;background:var(--footer-bg);font-family:"PT Sans Narrow",sans-serif;color:var(--footer-text)}
.foot-head{font-size:19px;color:#f5f5f5}
.foot-list{list-style:none;font-size:12px;line-height:20.8px}
.news-item{font-size:12px;line-height:14.5px;width:225px}
.news-item em{display:block}
.news-date{position:absolute;right:0;top:0}
.legal{left:0;top:1172px;width:1200px;height:28px;background:var(--legal-bg);color:#fff;font-family:"PT Sans Narrow",sans-serif;font-size:11px;text-align:center;line-height:28px}
</style>
</head>
<body>
<header class="abs site-header">
  <div class="abs brand">Petrova Careers</div>
  <div class="abs account-links">My Account Registered</div>
</header>
<nav class="abs main-nav">
  <ul>
    <li><svg width="20" height="18" viewBox="0 0 20 18" aria-label="Home"><path d="M10 1 1 9h3v8h4.5v-5h3v5H16V9h3z" fill="#fff"/></svg></li>
    <li>Categories</li><li>Get Stared</li><li>Brows Projects</li><li>Portfolios</li><li class="current">About Us</li>
  </ul>
</nav>

<h1 class="abs page-title">About Us</h1>
<section class="abs intro">
  <p>We need a design for the login page, about page, and inner pages of a recruitment site for an oil and gas company. Design should be modern, sleek, professional and colors can be blue, green, white, orange or any other recommended colors.</p>
  <p>Please also take into consideration that once the users login, they will need to access a form to fill in their information. We need a design for the login page, about page, and inner pages of a recruitment site for an oil and gas company. Design should be modern, sleek, professional and colors can be blue, green, white, orange or any other recommended colors.</p>
  <p style="margin-bottom:10px">We need a design for the login page, about page, and inner pages of a recruitment site for an oil and gas company. Design should be modern, sleek, professional and colors can be blue, green, white, orange or any other recommended colors.</p>
  <p>Read more on our <a href="#">how it works page</a>.</p>
</section>

<div class="abs rule" style="left:160px;top:428px;width:840px"></div>
<h2 class="abs mission-title">Our Mission Statement</h2>
<blockquote class="abs mission-quote">“We need a design for the login page, about page, and inner pages of a recruitment site for an oil and gas ”</blockquote>
<div class="abs rule" style="left:160px;top:537px;width:840px"></div>

<h2 class="abs section-title" style="left:182px;top:565px">Management Team</h2>
<div class="abs team-photo" style="left:212px;top:603px" role="img" aria-label="Portrait of the managing director"></div>
<h3 class="abs role" style="left:312px;top:601px;font-weight:400">Managing Director</h3>
<p class="abs bio" style="left:315px;top:629px">We need a design for the login page, about page, and inner pages of a recruitment site for an oil and gas company. Design should be modern, sleek, professional and colors can be blue, green, white, orange or any other recommended colors.</p>
<div class="abs team-photo" style="left:212px;top:728px;height:88px" role="img" aria-label="Portrait of the assistant managing director"></div>
<h3 class="abs role" style="left:310px;top:726px;font-weight:400">Assistant Managing</h3>
<p class="abs bio" style="left:313px;top:761px">We need a design for the login page, about page, and inner pages of a recruitment site for an oil and gas company. Design should be modern, sleek, professional and colors can be blue, green, white, orange or any other recommended colors.</p>

<div class="abs rule" style="left:160px;top:851px;width:840px"></div>
<h2 class="abs info-head" style="left:191px;top:867px;font-weight:400">Company Information</h2>
<div class="abs" style="left:190px;top:898px">
  <div class="info-label">Incorporation</div>
  <div class="info-text">Oil and Gas Pty Ltd<br>ABN: 48 913 605 227</div>
</div>
<div class="abs" style="left:484px;top:898px">
  <div class="info-label">Established</div>
  <div class="info-text" style="padding-left:3px;line-height:20px">July , 2010</div>
</div>
<div class="abs" style="left:690px;top:893px">
  <div class="info-label">Address</div>
  <div class="info-text">Level 4,<br>14 Marlow Street,<br>Kelton Heights 2040<br>NSW UAE</div>
</div>

<div class="abs footer-band"></div>
<footer class="abs site-footer">
  <div class="abs" style="left:203px;top:10px">
    <div class="foot-head">Support</div>
    <ul class="foot-list" style="margin:6px 0 0 3px"><li>Client Integration</li><li>Improved Performance</li><li>Customer Support</li><li>Our Business Helpline</li></ul>
  </div>
  <div class="abs" style="left:361px;top:12px">
    <div class="foot-head">Financial Success</div>
    <ul class="foot-list" style="margin:4px 0 0 5px"><li>Consequat Nunc Nibh</li><li>Improved Performance</li><li>Proin Cras Vault</li><li>Our Business Helpline</li><li>Voluptous</li></ul>
  </div>
  <div class="abs" style="left:541px;top:9px">
    <div class="foot-head">Business Guidelines</div>
    <ul class="foot-list" style="margin:13px 0 0 11px"><li>Client Integration</li><li>Improved Performance</li><li>Customer Support</li><li>Our Business Helpline</li></ul>
  </div>
  <div class="abs" style="left:743px;top:9px">
    <div class="foot-head">Latest News &amp; Events</div>
    <div class="news-item" style="position:relative;margin:16px 0 0 4px">Cras Quam Nibh Fullem Nest<em>Loresto mesemt maruis neterin</em><span class="news-date">4/21/11</span></div>
    <div class="news-item" style="position:relative;margin:15px 0 0 4px;width:218px">Mauris Netrern<em>Mesemt maruis neterin</em><span class="news-date">4/11/11</span></div>
  </div>
</footer>
<div class="abs legal">©2011 All Rights Reserved</div>
</body>
</html>
```